Outdoor Company Business Card design

We are an outdoor adventure company needing a business card. We sell outdoor adventures and clothing. Please use our logo in the business card. We are looking for something unique but delivers a clear message as to who we are. Please be creative

Target Market(s)

Outdoor adventures

Industry/Entity Type

Business

Contact Information for Business Card

Business name: TrailBrook If using the logo, no need to have a spot for the name
Owner / CEO: Owen Pardle
Website: TrailBrook.example
Facebook: Facebook.com/TrailBrook
Instagram: @pardle_owen
phone number: 555-384-7120
Email: Pardleteams@TrailBrook.example

Colors

Designer to choose colors to be used in the design.

Requirements
Must have
• The business card must include the details mentioned above. ie logo, my name, email, facebook, instagram, website, and phone number.
Should not have
• should not be cluttered or look messy

```html
<!DOCTYPE html>
<html lang="en">
<head>
<meta charset="utf-8">
<title>TrailBrook Business Card</title>
<link rel="stylesheet" href="https://fonts.googleapis.com/css2?family=Jost:wght@400;500;600;700&display=swap">
<style>
  :root {
    --page: #8f8f8f;
    --blue: #1165ab;
    --snow: #d9d9dc;
    --stone: #8a8a8d;
    --orange: #d14b22;
    --orange-light: #e3866a;
    --white: #f2f2f2;
  }
  html, body {
    margin: 0;
    padding: 0;
    width: 1105px;
    height: 1200px;
    overflow: hidden;
    background: var(--page);
    font-family: "Jost", sans-serif;
  }
  .canvas {
    position: relative;
    width: 1105px;
    height: 1200px;
  }
  .card {
    position: absolute;
    left: 182px;
    width: 749px;
    height: 428px;
    overflow: hidden;
  }
  .card--front { top: 118px; background: var(--blue); }
  .card--back  { top: 635px; background: var(--orange); }

  /* front */
  .front-ground {
    position: absolute;
    left: 0;
    top: 0;
    width: 749px;
    height: 428px;
  }
  .front-scene {
    position: absolute;
    left: 24px;
    top: 150px;
    width: 700px;
    height: 175px;
    border-radius: 90px 12px 0 0;
    background: linear-gradient(100deg, var(--orange) 0%, #c98a74 18%, var(--stone) 40%, #b9bcc4 62%, #7fa2c6 82%, var(--snow) 100%);
    opacity: 0.9;
  }
  .contact {
    position: absolute;
    left: 34px;
    top: 22px;
    margin: 0;
    padding: 0;
    list-style: none;
    color: var(--white);
    font-size: 17px;
    line-height: 24px;
  }
  .contact li { display: flex; align-items: center; gap: 10px; }
  .contact svg { width: 15px; height: 15px; flex: none; }
  .social-mark {
    display: inline-block;
    width: 13px;
    height: 13px;
    flex: none;
    box-sizing: border-box;
    border: 1.5px solid var(--white);
    border-radius: 2px;
  }
  .social-mark--inline { margin-left: 6px; }
  .holder {
    position: absolute;
    right: 46px;
    top: 36px;
    text-align: right;
    color: var(--white);
    text-transform: uppercase;
  }
  .holder__name { font-weight: 700; font-size: 30px; line-height: 30px; letter-spacing: 0.5px; }
  .holder__title { font-weight: 600; font-size: 20px; line-height: 24px; letter-spacing: 1px; }
  .front-brand {
    position: absolute;
    left: 0;
    right: 0;
    top: 330px;
    text-align center;
    text-align: center;
    color: var(--blue);
    font-weight: 500;
    font-size: 68px;
    line-height: 68px;
    letter-spacing: 2px;
  }

  /* back */
  .back-emblem {
    position: absolute;
    left: 246px;
    top: 135px;
    width: 258px;
    height: 90px;
    border-radius: 40px 6px 4px 4px;
    background: linear-gradient(180deg, var(--orange-light), #e8d6cf 60%, var(--orange));
    opacity: 0.85;
  }
  .back-brand {
    position: absolute;
    left: 0;
    right: 0;
    top: 226px;
    text-align: center;
    color: var(--white);
    font-weight: 500;
    font-size: 62px;
    line-height: 62px;
    letter-spacing: 1px;
  }
  .back-url {
    position: absolute;
    left: 0;
    right: 0;
    top: 334px;
    text-align: center;
    color: var(--white);
    font-size: 17px;
    letter-spacing: 6px;
  }
</style>
</head>
<body>
<main class="canvas">
  <section class="card card--front">
    <svg class="front-ground" viewBox="0 0 749 428" aria-hidden="true">
      <path d="M0 270 C150 250 320 330 520 330 C620 330 700 325 749 318 L749 428 L0 428 Z" fill="#d9d9dc"/>
    </svg>
    <div class="front-scene" role="img" aria-label="Illustration of an eagle, antlers and a duck before snowy mountain peaks"></div>
    <svg class="front-ground" viewBox="0 0 749 428" aria-hidden="true">
      <path d="M0 325 L749 325 L749 428 L0 428 Z" fill="#d9d9dc"/>
    </svg>
    <ul class="contact">
      <li>
        <svg viewBox="0 0 16 16"><path fill="#f2f2f2" d="M3 1l3 3-2 2c1 2 3 4 5 5l2-2 3 3-2 3C7 15 1 9 1 3z"/></svg>
        555-384-7120
      </li>
      <li>
        <svg viewBox="0 0 16 16"><rect x="1" y="3" width="14" height="10" fill="none" stroke="#f2f2f2" stroke-width="1.5"/><path d="M1 3l7 6 7-6" fill="none" stroke="#f2f2f2" stroke-width="1.5"/></svg>
        Pardleteams@TrailBrook.example
      </li>
      <li>
        <svg viewBox="0 0 16 16"><circle cx="8" cy="8" r="6.5" fill="none" stroke="#f2f2f2" stroke-width="1.5"/><path d="M1.5 8h13M8 1.5c-3 3-3 10 0 13M8 1.5c3 3 3 10 0 13" fill="none" stroke="#f2f2f2" stroke-width="1.2"/></svg>
        www.TrailBrook.example
      </li>
      <li>
        <span class="social-mark"></span>
        /TrailBrook
        <span class="social-mark social-mark--inline"></span>
        @pardle_owen
      </li>
    </ul>
    <div class="holder">
      <div class="holder__name">Owen Pardle</div>
      <div class="holder__title">Owner / CEO</div>
    </div>
    <div class="front-brand">TRAILBROOK</div>
  </section>

  <section class="card card--back">
    <div class="back-emblem" role="img" aria-label="Small emblem illustration of an eagle, antlers and mountains"></div>
    <div class="back-brand">TRAILBROOK</div>
    <div class="back-url">WWW.TRAILBROOK.EXAMPLE</div>
  </section>
</main>
</body>
</html>
```